Brightwell Harbor Property Maintenance and Construction Company require new business card design

We are a property maintenance and construction company that offer a total range of property maintenance construction services and have been too busy dealing with the running of the office and completing jobs to update our business cards. We have recently had a new logo designed for us and are needing to update our cards (and we also have new staff requiring business cards. We would ideally want to stay with the orange, black and grey theme. I have attached current business cards and also our new logo. Looking forward to feedback and ideas.

Target Market(s)

Real estate agents, local governments, companies, residential

Industry/Entity Type

Property Maintenance

Contact Information for Business Card

File uploaded has names and phone numbers for staff. We also need to add a card for a new staff member, which can be provided.

Colors
f37022

Requirements
Must have
• Must have logos for Certified Fabrication Steward and Prime Erector for which we are members of. Also a description of what services we provide
Should not have
• any "flowery" fonts and design. We are a construction company, so probably something very standard...but also not just a regular font (ie Arial!)

```html
<!DOCTYPE html>
<html lang="en">
<head>
<meta charset="utf-8">
<title>Brightwell Harbor Property Services – Business Cards</title>
<link rel="stylesheet" href="https://fonts.googleapis.com/css2?family=Open+Sans:wght@400;600;700&display=swap">
<style>
  :root {
    --orange: #f37022;
    --orange-light: #f7a04a;
    --peach: #f6c3a4;
    --grey: #8b8c8e;
    --grey-dark: #6f7072;
    --grey-light: #a3a4a6;
    --white: #ffffff;
    --stage: #ebe9e5;
  }
  * { box-sizing: border-box; margin: 0; padding: 0; }
  html, body { width: 1200px; height: 1000px; overflow: hidden; }
  body {
    background: var(--stage);
    font-family: "Open Sans", sans-serif;
    position: relative;
  }
  .card {
    position: absolute;
    width: 780px;
    height: 440px;
    overflow: hidden;
    box-shadow: 0 6px 18px rgba(0,0,0,0.18);
  }
  .card-front { left: 60px; top: 40px; }
  .card-back { left: 360px; top: 520px; }
  .card-bg { position: absolute; inset: 0; width: 100%; height: 100%; }

  /* member badges */
  .badge { position: absolute; width: 100px; height: 56px; }
  .badge-steward { left: 22px; top: 22px; }
  .badge-erector { right: 22px; top: 22px; }

  /* brand */
  .brand {
    position: absolute; left: 120px; top: 150px;
    display: flex; flex-direction: column; align-items: flex-start;
  }
  .brand-row { display: flex; align-items: center; gap: 10px; }
  .brand-mark { width: 22px; height: 22px; background: var(--orange); }
  .brand-name {
    font-size: 38px; font-weight: 700; color: var(--orange);
    line-height: 1; letter-spacing: -0.5px;
  }
  .brand-tagline {
    margin-top: 8px; margin-left: 32px;
    background: var(--grey-dark); color: var(--white);
    font-size: 13px; font-weight: 600; letter-spacing: 5px;
    padding: 3px 10px;
  }

  /* staff */
  .staff { position: absolute; left: 250px; top: 330px; color: var(--white); }
  .staff-name {
    background: var(--grey); display: inline-block;
    font-size: 21px; font-weight: 700; padding: 4px 40px 4px 14px;
  }
  .staff-details { padding: 6px 14px 0; font-size: 13px; line-height: 1.45; }
  .staff-details li { list-style: none; display: flex; align-items: center; gap: 6px; }

  /* contact */
  .divider-v {
    position: absolute; left: 498px; top: 270px; width: 1.5px; height: 140px;
    background: var(--white);
  }
  .contact {
    position: absolute; left: 520px; top: 262px; color: var(--white);
    font-size: 13px; line-height: 1.5; list-style: none;
  }
  .contact li { display: flex; align-items: flex-start; gap: 8px; margin-bottom: 3px; }
  .icon { width: 13px; height: 13px; flex: none; margin-top: 3px; }

  /* back */
  .services-title {
    position: absolute; left: 0; top: 0; width: 100%; height: 62px;
    display: flex; align-items: center; padding-left: 40px;
    color: var(--white); font-size: 22px; font-weight: 700; letter-spacing: 0.5px;
  }
  .service-list {
    position: absolute; top: 98px; list-style: none; color: var(--white);
    font-size: 18px; line-height: 26px;
  }
  .service-list li { display: flex; align-items: center; gap: 10px; }
  .service-list-trades { left: 60px; }
  .service-list-programs { left: 440px; }
  .tick { width: 12px; height: 12px; flex: none; }
  .divider-services {
    position: absolute; left: 410px; top: 110px; width: 1.5px; height: 170px;
    background: var(--white);
  }
</style>
</head>
<body>

<!-- Front -->
<section class="card card-front" aria-label="Business card front">
  <svg class="card-bg" viewBox="0 0 780 440" preserveAspectRatio="none" aria-hidden="true">
    <defs>
      <linearGradient id="greyFront" x1="0" y1="0" x2="1" y2="1">
        <stop offset="0" stop-color="#9c9d9f"/><stop offset="1" stop-color="#7e7f81"/>
      </linearGradient>
      <linearGradient id="orangeFront" x1="0" y1="1" x2="1" y2="0">
        <stop offset="0" stop-color="#ef6a1d"/><stop offset="0.55" stop-color="#f7a04a"/><stop offset="1" stop-color="#f07a25"/>
      </linearGradient>
    </defs>
    <rect width="780" height="440" fill="url(#greyFront)"/>
    <polygon points="0,180 560,0 780,0 780,136 0,386" fill="#ffffff"/>
    <polygon points="0,386 780,136 780,150 0,400" fill="#f6c3a4"/>
    <polygon points="0,400 780,150 780,440 0,440" fill="url(#orangeFront)"/>
  </svg>

  <svg class="badge badge-steward" viewBox="0 0 100 56" role="img" aria-label="Certified Fabrication Steward member badge">
    <rect x="1" y="1" width="98" height="54" fill="none" stroke="#c9cacc" stroke-width="2"/>
    <circle cx="24" cy="28" r="13" fill="none" stroke="#c9cacc" stroke-width="2"/>
  </svg>
  <svg class="badge badge-erector" viewBox="0 0 100 56" role="img" aria-label="Prime Erector member badge">
    <rect x="1" y="1" width="98" height="54" fill="none" stroke="#a3a4a6" stroke-width="2"/>
    <circle cx="28" cy="28" r="14" fill="none" stroke="#a3a4a6" stroke-width="2"/>
  </svg>

  <div class="brand">
    <div class="brand-row">
      <span class="brand-mark"></span>
      <span class="brand-name">Brightwell Harbor</span>
    </div>
    <span class="brand-tagline">PROPERTY SERVICES</span>
  </div>

  <div class="staff">
    <h1 class="staff-name">Dana Whitcombe</h1>
    <ul class="staff-details">
      <li>Director</li>
      <li>Licence No: CBL 48217</li>
      <li>
        <svg class="icon" viewBox="0 0 12 12" aria-hidden="true"><rect x="2.5" y="0.5" width="7" height="11" rx="1.2" fill="none" stroke="#fff"/></svg>
        0400 555 318
      </li>
    </ul>
  </div>

  <span class="divider-v"></span>
  <ul class="contact">
    <li>
      <svg class="icon" viewBox="0 0 12 12" aria-hidden="true"><path d="M6 0.5a3.8 3.8 0 0 0-3.8 3.8C2.2 7.2 6 11.5 6 11.5s3.8-4.3 3.8-7.2A3.8 3.8 0 0 0 6 0.5z" fill="#fff"/><circle cx="6" cy="4.3" r="1.4" fill="#f39a44"/></svg>
      <span>42 Enterprise Way<br>Ashgrove Vic 3190</span>
    </li>
    <li>
      <svg class="icon" viewBox="0 0 12 12" aria-hidden="true"><path d="M2.5 0.8l2 2.2-1 1.4c.7 1.6 2 2.9 3.6 3.6l1.4-1 2.2 2-1 2C5 10.8 1.2 7 .8 1.8z" fill="#fff"/></svg>
      <span>1300 555 274</span>
    </li>
    <li>
      <svg class="icon" viewBox="0 0 12 12" aria-hidden="true"><rect x="0.5" y="2" width="11" height="8" fill="#fff"/><path d="M0.5 2l5.5 4.5L11.5 2" fill="none" stroke="#f39a44"/></svg>
      <span>dana@brightwellharbor.net.au</span>
    </li>
    <li>
      <svg class="icon" viewBox="0 0 12 12" aria-hidden="true"><circle cx="6" cy="6" r="5.3" fill="none" stroke="#fff"/><ellipse cx="6" cy="6" rx="2.3" ry="5.3" fill="none" stroke="#fff"/><path d="M0.7 6h10.6" stroke="#fff"/></svg>
      <span>www.brightwellharbor.net.au</span>
    </li>
  </ul>
</section>

<!-- Back -->
<section class="card card-back" aria-label="Business card back">
  <svg class="card-bg" viewBox="0 0 780 440" preserveAspectRatio="none" aria-hidden="true">
    <defs>
      <linearGradient id="orangeBack" x1="0" y1="0" x2="1" y2="1">
        <stop offset="0" stop-color="#ef6a1d"/><stop offset="0.5" stop-color="#f7a04a"/><stop offset="1" stop-color="#ee6c1e"/>
      </linearGradient>
    </defs>
    <rect width="780" height="440" fill="#8b8c8e"/>
    <polygon points="0,70 720,70 780,130 780,440 150,440 0,330" fill="url(#orangeBack)"/>
    <polygon points="0,330 150,440 128,440 0,346" fill="#f6c3a4"/>
    <polygon points="720,70 780,130 780,112 738,70" fill="#f6c3a4"/>
  </svg>

  <h2 class="services-title">OFFERING ALL PROPERTY MAINTENANCE SERVICES</h2>

  <ul class="service-list service-list-trades">
    <li><svg class="tick" viewBox="0 0 12 12" aria-hidden="true"><path d="M1 6.5l3 3L11 2" fill="none" stroke="#fff" stroke-width="2"/></svg>Carpentry</li>
    <li><svg class="tick" viewBox="0 0 12 12" aria-hidden="true"><path d="M1 6.5l3 3L11 2" fill="none" stroke="#fff" stroke-width="2"/></svg>Plumbing</li>
    <li><svg class="tick" viewBox="0 0 12 12" aria-hidden="true"><path d="M1 6.5l3 3L11 2" fill="none" stroke="#fff" stroke-width="2"/></svg>Electrical</li>
    <li><svg class="tick" viewBox="0 0 12 12" aria-hidden="true"><path d="M1 6.5l3 3L11 2" fill="none" stroke="#fff" stroke-width="2"/></svg>Painting</li>
    <li><svg class="tick" viewBox="0 0 12 12" aria-hidden="true"><path d="M1 6.5l3 3L11 2" fill="none" stroke="#fff" stroke-width="2"/></svg>Tiling</li>
    <li><svg class="tick" viewBox="0 0 12 12" aria-hidden="true"><path d="M1 6.5l3 3L11 2" fill="none" stroke="#fff" stroke-width="2"/></svg>Plastering</li>
    <li><svg class="tick" viewBox="0 0 12 12" aria-hidden="true"><path d="M1 6.5l3 3L11 2" fill="none" stroke="#fff" stroke-width="2"/></svg>Garden Maintenance</li>
    <li><svg class="tick" viewBox="0 0 12 12" aria-hidden="true"><path d="M1 6.5l3 3L11 2" fill="none" stroke="#fff" stroke-width="2"/></svg>Cleaning Services</li>
    <li><svg class="tick" viewBox="0 0 12 12" aria-hidden="true"><path d="M1 6.5l3 3L11 2" fill="none" stroke="#fff" stroke-width="2"/></svg>Waterproofing</li>
    <li><svg class="tick" viewBox="0 0 12 12" aria-hidden="true"><path d="M1 6.5l3 3L11 2" fill="none" stroke="#fff" stroke-width="2"/></svg>All Handyman Services</li>
  </ul>

  <span class="divider-services"></span>

  <ul class="service-list service-list-programs">
    <li><svg class="tick" viewBox="0 0 12 12" aria-hidden="true"><path d="M1 6.5l3 3L11 2" fill="none" stroke="#fff" stroke-width="2"/></svg>Programmed Maintenance</li>
    <li><svg class="tick" viewBox="0 0 12 12" aria-hidden="true"><path d="M1 6.5l3 3L11 2" fill="none" stroke="#fff" stroke-width="2"/></svg>Essential Services</li>
    <li><svg class="tick" viewBox="0 0 12 12" aria-hidden="true"><path d="M1 6.5l3 3L11 2" fill="none" stroke="#fff" stroke-width="2"/></svg>Maintenance Planning</li>
    <li><svg class="tick" viewBox="0 0 12 12" aria-hidden="true"><path d="M1 6.5l3 3L11 2" fill="none" stroke="#fff" stroke-width="2"/></svg>Reactionary Maintenance</li>
    <li><svg class="tick" viewBox="0 0 12 12" aria-hidden="true"><path d="M1 6.5l3 3L11 2" fill="none" stroke="#fff" stroke-width="2"/></svg>Commercial / Residential</li>
    <li><svg class="tick" viewBox="0 0 12 12" aria-hidden="true"><path d="M1 6.5l3 3L11 2" fill="none" stroke="#fff" stroke-width="2"/></svg>Body Corporate</li>
    <li><svg class="tick" viewBox="0 0 12 12" aria-hidden="true"><path d="M1 6.5l3 3L11 2" fill="none" stroke="#fff" stroke-width="2"/></svg>Insurance Claims</li>
    <li><svg class="tick" viewBox="0 0 12 12" aria-hidden="true"><path d="M1 6.5l3 3L11 2" fill="none" stroke="#fff" stroke-width="2"/></svg>24 Hour On Call</li>
  </ul>
</section>

</body>
</html>
```